italian food processing equipment manufacturer selling worldwide look for a new business card for al

Our headquarter is in Italy but we have different regional offices : Chicago, Moscow and Singapore, plus an agent in Brasil. We would like an image to exlain ONE TEAM, ONE MISSION, GLOBAL SOLUTION.

```html
<!DOCTYPE html>
<html lang="en">
<head>
<meta charset="utf-8">
<title>Vantero – Business Card</title>
<link rel="stylesheet" href="https://fonts.googleapis.com/css2?family=Alegreya:wght@400;700&display=swap">
<style>
  :root {
    --backdrop: #d9d6d1;
    --card-black: #0a0a0b;
    --card-glow: #1f2022;
    --brand-blue: #29abe2;
    --text-light: #ecebe8;
    --edge: #2a2a2c;
  }
  * { box-sizing: border-box; margin: 0; padding: 0; }
  html, body {
    width: 1200px;
    height: 900px;
    overflow: hidden;
    background: var(--backdrop);
    font-family: "Alegreya", Georgia, serif;
  }
  .sheet {
    width: 1200px;
    height: 900px;
    display: flex;
    flex-direction: column;
    align-items: center;
    justify-content: center;
    gap: 56px;
  }
  .card {
    position: relative;
    width: 660px;
    height: 378px;
    border-radius: 3px;
    background: radial-gradient(ellipse at 50% 35%, var(--card-glow) 0%, var(--card-black) 62%);
    box-shadow: 0 14px 30px rgba(0,0,0,0.28);
    border: 1px solid var(--edge);
    overflow: hidden;
  }
  .wordmark {
    position: absolute;
    color: var(--brand-blue);
    font-weight: 700;
    letter-spacing: 0.04em;
    line-height: 1;
    display: flex;
    align-items: center;
    gap: 12px;
  }
  .wordmark__square {
    width: 0.42em;
    height: 0.42em;
    background: var(--brand-blue);
  }
  .card--front .wordmark {
    font-size: 72px;
    left: 50%;
    top: 50%;
    transform: translate(-50%, -58%);
  }
  .card--back .wordmark {
    font-size: 58px;
    right: 40px;
    top: 40px;
  }
  .contact {
    position: absolute;
    left: 44px;
    bottom: 38px;
    color: var(--text-light);
    font-size: 16px;
    font-style: normal;
    line-height: 1.45;
  }
  .contact__name {
    font-size: 27px;
    font-weight: 700;
    line-height: 1.1;
  }
  .contact__role {
    color: var(--brand-blue);
    font-size: 18px;
    margin-bottom: 34px;
  }
  .contact__label,
  .contact__web { color: var(--brand-blue); }
  .contact__line span + span { margin-left: 8px; }
</style>
</head>
<body>
  <main class="sheet">
    <section class="card card--front" aria-label="Card front">
      <div class="wordmark"><span class="wordmark__square"></span>VANTERO</div>
    </section>

    <section class="card card--back" aria-label="Card back">
      <div class="wordmark">VANTERO</div>
      <address class="contact">
        <p class="contact__name">Marco Bellini</p>
        <p class="contact__role">Managing Director</p>
        <p class="contact__line">Via Selice 48, Imola, Italy, 40026</p>
        <p class="contact__line">
          <span><span class="contact__label">T:</span>(039) 054 261 020</span>
          <span><span class="contact__label">F:</span>(039) 054261021</span>
          <span><span class="contact__label">M:</span>(039)335482917</span>
        </p>
        <p class="contact__line">
          <span><span class="contact__label">E:</span> info@vantero.example</span>
          <span class="contact__web">www.vantero.example</span>
        </p>
      </address>
    </section>
  </main>
</body>
</html>
```